Family history tech product tailored for moms needs banner ads

plume.com is launching next week and we've partnered with an ad group that will be launching a campaign on school district websites that will be pushed to 250k moms of school age children.

We're launching a $199 product that shows you more about who you are through your family's history. We connect people wanting to learn more about themselves with expert researcher/genealogist who will uncover their past and find the stories of their ancestors.

See branding guidelines below as well as the landing page we're designing where these ads will take you.

Here is the landing page design:
https://chatbox-files.example/X839KQ2M1-G72P4TTR8-kf4e1mzq90

Target Market(s)

Mom's of kids in elementary and middle school.

Persona:
Mom, 38 years old, 2 kids (age 6 and 8)
Lives in Dallas, drives a 2016 Vormak Ridgel
She and husband met in college. She was a nurse, but she stopped working to be a full-time mom
Husband is in financial consulting, household income of $140,000
When kids at school, she runs errands, works out, meets up with girlfriends for coffee
She shops at Sorvanta, has active hobbies
She is always busy, there’s not enough time for her family; she is worried that her kids may become distant because of how busy the family is
She values time with family most, soccer weekends, financial stability, college for the kids
Wants to connect more with the kids and the family to increase the bond, and she thinking having more context for the family will help them bond around a common history
Her objections to Plume are lack of trust in a new service, time it will cost her to get the info she wants to achieve her goals

Industry/Entity Type

Startup

Font styles to use
Other font styles liked:
• follow style guide

Requirements
Must have
• Must follow the design pattern in our branding guide.
• https://www.filecrate.example/s/kqm4tnw819zpxa/Screenshot%202016-11-30%2013.39.48.png?dl=0
Nice to have
• Good copy, I'm less worried about that though. We can work together on that.
Should not have
• Stock imagery that sucks. I'm really opposed to anything that looks like it is from the 2001 - 2011

```html
<!DOCTYPE html>
<html lang="en">
<head>
<meta charset="utf-8">
<title>Plume banner set</title>
<link rel="stylesheet" href="https://fonts.googleapis.com/css2?family=Raleway:wght@400;500;600;700;800&display=swap">
<style>
  :root {
    --brand-blue: #3d9ff0;
    --button-blue: #72bcf6;
    --white: #ffffff;
    --page-bg: #eceff2;
    --ring-pink: #d46aa2;
    --ring-lime: #c6d43a;
    --ring-teal: #7fb4c9;
    --ring-green: #7dbf4b;
    --ring-orange: #e9874f;
    --photo-tone: #9a948e;
    --dot-blue: #63b2f4;
  }
  * { box-sizing: border-box; margin: 0; padding: 0; }
  html, body { width: 1200px; height: 869px; overflow: hidden; }
  body {
    background: var(--page-bg);
    font-family: "Raleway", sans-serif;
    position: relative;
  }
  .banner {
    position: absolute;
    background: var(--brand-blue);
    color: var(--white);
    overflow: hidden;
    box-shadow: 0 6px 14px rgba(0,0,0,0.18);
  }
  .banner svg.art { position: absolute; left: 0; top: 0; }
  .headline { font-weight: 700; line-height: 1.05; }
  .subline { font-weight: 400; }
  .brand-name {
    position: absolute;
    font-family: "Raleway", sans-serif;
    font-weight: 800;
    color: var(--brand-blue);
    letter-spacing: -0.5px;
  }
  .cta {
    position: absolute;
    background: var(--button-blue);
    border-radius: 999px;
    box-shadow: 0 3px 6px rgba(0,0,0,0.15);
    color: var(--white);
    font-weight: 700;
    display: flex;
    align-items: center;
    gap: 10px;
  }
  .cta svg { flex: none; }

  /* Skyscraper */
  .skyscraper { left: 69px; top: 74px; width: 187px; height: 710px; }
  .skyscraper .headline { position: absolute; left: 0; right: 0; top: 28px; text-align: center; font-size: 37px; }
  .skyscraper .subline { position: absolute; left: 0; right: 0; top: 122px; text-align: center; font-size: 20px; line-height: 1.2; }
  .benefits { position: absolute; left: 13px; top: 208px; list-style: none; }
  .benefits li { display: flex; align-items: center; gap: 9px; font-size: 18px; font-weight: 500; height: 36px; }
  .skyscraper .cta { left: 14px; top: 354px; width: 158px; height: 54px; padding-left: 22px; font-size: 15px; line-height: 1.15; }
  .skyscraper .cta small { display: block; font-size: 13px; font-weight: 600; padding-left: 6px; }
  .skyscraper .brand-name { left: 0; right: 0; top: 612px; text-align: center; font-size: 48px; }

  /* Leaderboard */
  .leaderboard { left: 280px; top: 75px; width: 858px; height: 109px; }
  .leaderboard .brand-name { left: 20px; top: 28px; font-size: 38px; }
  .leaderboard .headline { position: absolute; left: 155px; top: 17px; font-size: 34px; }
  .leaderboard .subline { position: absolute; left: 157px; top: 58px; font-size: 21px; }
  .leaderboard .cta { left: 675px; top: 25px; width: 158px; height: 54px; padding-left: 22px; font-size: 16px; line-height: 1.1; }
  .leaderboard .cta small { display: block; font-size: 13px; font-weight: 600; padding-left: 14px; }

  /* Square */
  .square { left: 280px; top: 285px; width: 355px; height: 291px; }
  .square .headline { position: absolute; left: 0; right: 0; top: 24px; text-align: center; font-size: 37px; }
  .square .subline { position: absolute; left: 0; right: 0; top: 66px; text-align: center; font-size: 20px; }
  .square .cta { left: 58px; top: 111px; width: 240px; height: 40px; justify-content: center; font-size: 15px; }
  .square .brand-name { left: 0; right: 0; top: 240px; text-align: center; font-size: 38px; }
</style>
</head>
<body>

<!-- Skyscraper 160x600 -->
<section class="banner skyscraper">
  <svg class="art" width="187" height="710" viewBox="0 0 187 710">
    <circle cx="30" cy="450" r="9" fill="var(--dot-blue)"/>
    <circle cx="170" cy="455" r="7" fill="var(--dot-blue)"/>
    <path d="M0 600 Q90 575 187 592 V710 H0 Z" fill="var(--white)"/>
    <g role="img" aria-label="Portrait photos of family members in speech bubbles">
      <path d="M5 560 L-10 620 L40 585 Z" fill="var(--ring-pink)"/>
      <circle cx="25" cy="520" r="55" fill="var(--ring-pink)"/>
      <circle cx="25" cy="520" r="42" fill="var(--photo-tone)"/>
      <path d="M170 555 L190 590 L150 565 Z" fill="var(--ring-green)"/>
      <circle cx="172" cy="528" r="36" fill="var(--ring-green)"/>
      <circle cx="172" cy="528" r="27" fill="var(--photo-tone)"/>
      <circle cx="128" cy="468" r="25" fill="var(--ring-lime)"/>
      <circle cx="128" cy="468" r="18" fill="var(--photo-tone)"/>
      <path d="M70 590 L80 625 L100 595 Z" fill="var(--ring-teal)"/>
      <circle cx="92" cy="545" r="57" fill="var(--ring-teal)"/>
      <circle cx="92" cy="545" r="44" fill="#c9c2ba"/>
    </g>
  </svg>
  <h2 class="headline">Are You<br>Belong</h2>
  <p class="subline">To A Family<br>Narrative ?</p>
  <ul class="benefits">
    <li><svg width="20" height="20" viewBox="0 0 20 20"><circle cx="10" cy="10" r="10" fill="var(--white)"/><path d="M5.5 10.5 L8.5 13.5 L14.5 7" stroke="var(--brand-blue)" stroke-width="2.4" fill="none"/></svg>Get Stories</li>
    <li><svg width="20" height="20" viewBox="0 0 20 20"><circle cx="10" cy="10" r="10" fill="var(--white)"/><path d="M5.5 10.5 L8.5 13.5 L14.5 7" stroke="var(--brand-blue)" stroke-width="2.4" fill="none"/></svg>Get Pictures</li>
    <li><svg width="20" height="20" viewBox="0 0 20 20"><circle cx="10" cy="10" r="10" fill="var(--white)"/><path d="M5.5 10.5 L8.5 13.5 L14.5 7" stroke="var(--brand-blue)" stroke-width="2.4" fill="none"/></svg>Get Memories</li>
  </ul>
  <div class="cta">
    <svg width="16" height="22" viewBox="0 0 16 22"><path d="M1 1 L1 17 L5 13 L8 20 L11 19 L8 12 L14 12 Z" fill="var(--white)"/></svg>
    <span>Lets Find<small>Out Them</small></span>
  </div>
  <div class="brand-name">plume</div>
</section>

<!-- Leaderboard 728x90 -->
<section class="banner leaderboard">
  <svg class="art" width="858" height="109" viewBox="0 0 858 109">
    <path d="M0 0 H128 Q150 55 128 109 H0 Z" fill="var(--white)"/>
    <circle cx="470" cy="30" r="8" fill="var(--dot-blue)"/>
    <circle cx="655" cy="85" r="7" fill="var(--dot-blue)"/>
    <g role="img" aria-label="Portrait photos of family members in speech bubbles">
      <circle cx="497" cy="68" r="22" fill="var(--ring-lime)"/>
      <circle cx="497" cy="68" r="16" fill="var(--photo-tone)"/>
      <circle cx="547" cy="55" r="40" fill="var(--ring-pink)"/>
      <circle cx="547" cy="55" r="31" fill="var(--photo-tone)"/>
      <circle cx="600" cy="12" r="28" fill="var(--ring-green)"/>
      <circle cx="600" cy="12" r="20" fill="var(--photo-tone)"/>
      <circle cx="602" cy="72" r="40" fill="var(--ring-teal)"/>
      <circle cx="602" cy="72" r="31" fill="#c9c2ba"/>
    </g>
  </svg>
  <div class="brand-name">plume</div>
  <h2 class="headline">Are You Belong</h2>
  <p class="subline">To A Family Narrative ?</p>
  <div class="cta">
    <svg width="16" height="22" viewBox="0 0 16 22"><path d="M1 1 L1 17 L5 13 L8 20 L11 19 L8 12 L14 12 Z" fill="var(--white)"/></svg>
    <span>Lets Find<small>Out Them</small></span>
  </div>
</section>

<!-- Medium rectangle 300x250 -->
<section class="banner square">
  <svg class="art" width="355" height="291" viewBox="0 0 355 291">
    <circle cx="30" cy="178" r="8" fill="var(--dot-blue)"/>
    <circle cx="325" cy="170" r="7" fill="var(--dot-blue)"/>
    <path d="M0 222 Q90 200 180 214 Q270 228 355 205 V291 H0 Z" fill="var(--white)"/>
    <g role="img" aria-label="Portrait photos of family members in speech bubbles">
      <circle cx="72" cy="198" r="18" fill="var(--ring-orange)"/>
      <circle cx="72" cy="198" r="13" fill="var(--photo-tone)"/>
      <circle cx="128" cy="186" r="28" fill="var(--ring-pink)"/>
      <circle cx="128" cy="186" r="21" fill="var(--photo-tone)"/>
      <circle cx="233" cy="184" r="22" fill="var(--ring-green)"/>
      <circle cx="233" cy="184" r="16" fill="var(--photo-tone)"/>
      <circle cx="285" cy="195" r="18" fill="var(--ring-lime)"/>
      <circle cx="285" cy="195" r="13" fill="var(--photo-tone)"/>
      <circle cx="180" cy="196" r="30" fill="var(--ring-teal)"/>
      <circle cx="180" cy="196" r="23" fill="#c9c2ba"/>
    </g>
  </svg>
  <h2 class="headline">Are You Belong</h2>
  <p class="subline">To A Family Narrative ?</p>
  <div class="cta">
    <svg width="13" height="18" viewBox="0 0 16 22"><path d="M1 1 L1 17 L5 13 L8 20 L11 19 L8 12 L14 12 Z" fill="var(--white)"/></svg>
    <span>Lets Find Out Them</span>
  </div>
  <div class="brand-name">plume</div>
</section>

</body>
</html>
```